High profile consultancy

We need a web design for a company called VN Services. VN as abbreviation for Verdant North.

Company focusses on Sourcing (VN Sourcing, focus on ICT), Metrics (VN Metrics; focus on business case analysis and trends in ICT) and Software (VN software; to be developed later on; mainly tools supporting VN soucing and metrics)

Customers base consists of large enterprises, >1000 employees.

Site needs to have menu's for
- services
- login
- about
and a special area ' inspire ' to be able to communicate topics that should inspire our customers to contact us.

but key; it schould communicate our expertise and focus on deep knowlegde of ICT sourcing

Reason: please advice on content management systems to be used to maintain site also please advice on Plimzo search bidlines. Will provide feedback on designs shortly.

Target Market(s)

CIO's; board of directors;
company excels in ICT / business knowledge and ability to execute; creates / optimizes relations between ICT suppliers and enterprises.

Requirements
Must have
• website should be easily be found; adaptive by design; accessible by all browsers.
• Need to have a login section for later use
Nice to have
• usage of (draft) logo. see upload.

```html
<!DOCTYPE html>
<html lang="en">
<head>
<meta charset="utf-8">
<title>VN Services – Verdant North</title>
<link href="https://fonts.googleapis.com/css2?family=Arimo:wght@400;700&family=Open+Sans:wght@400;600&family=Roboto+Condensed:wght@700&display=swap" rel="stylesheet">
<style>
:root{
  --navy:#1b3556;
  --footer:#10233c;
  --footer-deep:#0a1729;
  --menu:#3b3b3b;
  --blue:#2a6db5;
  --blue-dark:#1d4f8a;
  --red:#c0272d;
  --text:#333;
  --muted:#666;
  --panel:#efefef;
  --panel-head:#e1e1e1;
  --line:#d8d8d8;
  --star:#f1b51c;
}
*{box-sizing:border-box;margin:0;padding:0}
html,body{width:853px;height:1200px;overflow:hidden;background:#fff}
body{position:relative;font-family:"Arimo",Arial,sans-serif;color:var(--text);font-size:9px}
.abs{position:absolute}
a{color:inherit;text-decoration:none}

.top-band{left:0;top:0;width:853px;height:8px;background:var(--navy)}
.brand{left:96px;top:36px;display:flex;align-items:center;gap:7px}
.brand-dot{width:22px;height:22px;border-radius:50%;background:var(--blue-dark)}
.brand-name{font-family:"Open Sans",sans-serif;font-size:19px;color:#555;letter-spacing:.3px}
.account-links{right:84px;top:25px;font-family:"Open Sans",sans-serif;font-size:8px;color:#444}
.account-links a{color:var(--blue)}
.contact-line{right:84px;top:47px;font-family:"Open Sans",sans-serif;font-size:8px;color:var(--blue);display:flex;gap:10px;align-items:center}
.contact-line span{display:flex;align-items:center;gap:3px}
.top-nav{right:84px;top:67px;display:flex;gap:20px;font-family:"Open Sans",sans-serif;font-size:9.5px;color:#333}

.main-menu{left:85px;top:87px;width:684px;height:20px;background:var(--menu);display:flex;font-family:"Open Sans",sans-serif;font-size:9.5px;color:#fff}
.main-menu a{display:flex;align-items:center;justify-content:center;border-right:1px solid #666;height:100%}
.main-menu a:last-child{border-right:0}

.hero{left:85px;top:107px;width:684px;height:189px;background:linear-gradient(90deg,#f2f2f2 0%,#e6e6e6 45%,#d9d9d9 100%)}
.hero-people{right:0;top:0;width:340px;height:189px;background:linear-gradient(90deg,rgba(220,220,220,0) 0%,#c9ccd3 40%,#9aa9c0 75%,#c7ccd6 100%)}
.hero-title{left:30px;top:70px;font-family:"Roboto Condensed",sans-serif;font-weight:700;font-size:27px;color:#1d5aa3;letter-spacing:.3px}
.hero-sub{left:32px;top:100px;font-family:"Open Sans",sans-serif;font-size:17px;color:var(--red)}

.service-card{top:307px;height:63px;background:linear-gradient(#fff,#eee);border-bottom:2px solid #ccc}
.service-card::before{content:"";position:absolute;left:0;top:0;border-top:10px solid var(--blue-dark);border-right:10px solid transparent}
.service-card h3{position:absolute;left:8px;top:9px;font-family:"Open Sans",sans-serif;font-weight:400;font-size:10px;color:var(--blue)}
.service-card p{position:absolute;left:8px;top:23px;width:110px;font-family:"Open Sans",sans-serif;font-size:7px;line-height:10.5px;color:var(--muted)}
.service-photo{position:absolute;right:0;top:0;width:92px;height:63px}

.welcome{left:85px;top:383px;width:684px;height:169px;background:#f8f8f8;border:1px solid var(--line);border-bottom:2px solid #ccc}
.welcome h2{position:absolute;left:11px;top:12px;font-weight:400;font-size:13px;color:#333}
.welcome h2 span,.accent{color:var(--blue)}
.welcome p{position:absolute;left:11px;width:436px;font-size:8.6px;line-height:12.8px;color:#333}
.portrait-ring{left:540px;top:384px;width:208px;height:208px;border-radius:50%;background:#fff;box-shadow:0 2px 6px rgba(0,0,0,.25);padding:7px}
.portrait{width:100%;height:100%;border-radius:50%;background:radial-gradient(circle at 50% 45%,#d9c9b6 0%,#b9aa95 45%,#8b9bb0 100%)}

.who{left:85px;top:567px;width:684px;height:137px;background:var(--panel);border-top:3px solid #ddd}
.who-photo{left:13px;top:14px;width:180px;height:107px;border:3px solid #fff;box-shadow:0 0 2px rgba(0,0,0,.3);background:linear-gradient(90deg,#c9cdd4,#8d98a8 50%,#d6d3cf)}
.who h2{position:absolute;left:208px;top:29px;font-weight:400;font-size:11.5px;color:#222}
.who p{position:absolute;left:208px;top:46px;width:465px;font-size:8.3px;line-height:12.7px;color:#333}
.who .more{position:absolute;right:62px;top:112px;font-size:8.3px;color:var(--blue-dark)}

.panel{top:717px;background:var(--panel);border-bottom:3px solid #ddd}
.panel-head{height:21px;background:var(--panel-head);display:flex;align-items:center;padding-left:4px;gap:8px;font-size:10.5px;font-weight:700;color:var(--blue-dark)}
.panel-head::before{content:"";width:4px;height:14px;border-left:1.5px solid var(--blue-dark);border-right:1.5px solid var(--blue-dark)}
.panel h3{position:absolute;font-weight:400;font-size:11px;color:#222}
.panel p{position:absolute;font-size:8.3px;line-height:12.7px;color:#333}
.thumb{position:absolute;border:3px solid #fff;box-shadow:0 0 2px rgba(0,0,0,.3)}

.topic{position:absolute;left:8px;display:flex;gap:8px}
.topic-image{width:41px;height:41px;background:linear-gradient(#9fb4c8,#5d7893)}
.topic b{display:block;font-weight:400;font-size:8.5px;color:var(--muted);margin-top:1px}
.topic span{display:block;font-size:8.5px;color:#222;margin-top:3px}
.stars{display:flex;gap:3px;margin-top:3px}

.client-head{left:87px;top:914px;width:681px;height:20px}
.clients{left:100px;top:972px;width:640px;display:flex;justify-content:space-between;align-items:center;font-family:"Open Sans",sans-serif;font-size:13px;color:#777}
.clients span{display:flex;align-items:center;gap:5px}
.clients i{display:inline-block;width:7px;height:7px;border-radius:50%;background:#888}

.footer{left:0;top:1032px;width:853px;height:135px;background:var(--footer)}
.foot-col{position:absolute;top:36px;width:128px;font-family:"Open Sans",sans-serif}
.foot-col h4{font-weight:400;font-size:9.5px;color:#8fa1b8;padding-bottom:7px;border-bottom:1px solid #2c4160}
.foot-col a{display:block;font-size:9px;color:#a9b6c7;padding:4px 0 4px 1px;border-bottom:1px solid #2c4160}
.foot-col a:last-child{border-bottom:0}
.newsletter{left:603px;top:36px;width:163px;font-family:"Open Sans",sans-serif}
.newsletter h4{font-weight:400;font-size:10.5px;color:#b6c2d2;display:flex;align-items:center;gap:4px}
.news-form{display:flex;margin-top:8px;height:21px}
.news-form .field{flex:1;background:#fff}
.news-form .btn{width:42px;background:var(--red);color:#fff;font-size:9px;display:flex;align-items:center;justify-content:center}
.social{display:flex;justify-content:flex-end;gap:7px;margin-top:9px;font-size:7.5px;color:#a9b6c7}
.social span{display:flex;align-items:center;gap:2px}
.social i{width:7px;height:7px;border-radius:50%;background:#a9b6c7;display:inline-block}
.bottom-bar{left:0;top:1167px;width:853px;height:33px;background:var(--footer-deep)}
.copyright{left:93px;top:12px;font-family:"Open Sans",sans-serif;font-size:7px;color:#8795a8}
.payments{right:91px;top:8px;display:flex;gap:5px}
.payments span{height:17px;padding:0 5px;background:#e6e6e6;border-radius:2px;font-family:"Open Sans",sans-serif;font-size:7.5px;color:#555;display:flex;align-items:center}
</style>
</head>
<body>

<div class="abs top-band"></div>

<header>
  <div class="abs brand"><span class="brand-dot"></span><span class="brand-name">VN Services</span></div>
  <div class="abs account-links"><a href="#">Login</a> | Become a Member <a href="#">Sign up</a></div>
  <div class="abs contact-line">
    <span><svg width="8" height="8" viewBox="0 0 10 10"><path d="M2 1l2 2-1 1.5c.8 1.5 1.7 2.4 3 3L7.5 6l2 2-1.5 1.5C4.5 9 1 5.5.5 2.5z" fill="#888"/></svg>0800-555 0142</span>
    <span><svg width="9" height="7" viewBox="0 0 10 8"><rect x=".5" y=".5" width="9" height="7" fill="none" stroke="#888"/><path d="M.5.5L5 4.5 9.5.5" fill="none" stroke="#888"/></svg>info@vnservices.example</span>
  </div>
  <nav class="abs top-nav"><a href="#">Home</a><a href="#">About</a><a href="#">Services</a><a href="#">Contact</a></nav>
</header>

<nav class="abs main-menu">
  <a href="#" style="width:123px">VN Sourcing</a>
  <a href="#" style="width:175px">VN Metrics</a>
  <a href="#" style="width:121px">VN Software</a>
  <a href="#" style="width:156px">Inspire</a>
  <a href="#" style="width:109px">About</a>
</nav>

<section class="abs hero" role="img" aria-label="Office backdrop with a team of ICT consultants">
  <div class="abs hero-people"></div>
  <div class="abs hero-title">ICT SOURCING &amp; METRICS</div>
  <div class="abs hero-sub">Deep ICT Knowledge, Proven Execution</div>
</section>

<article class="abs service-card" style="left:85px;width:216px">
  <h3>VN Sourcing</h3>
  <p>Selecting and managing the right ICT suppliers.</p>
  <div class="service-photo" role="img" aria-label="Photo of consultants in an office" style="background:linear-gradient(90deg,#e8e8e8,#8f8f98 60%,#c9c9c9)"></div>
</article>
<article class="abs service-card" style="left:321px;width:215px">
  <h3>VN Metrics</h3>
  <p>Business cases and trends in ICT, made clear.</p>
  <div class="service-photo" role="img" aria-label="Photo of a team reviewing figures around a desk" style="background:linear-gradient(135deg,#5a7fa8,#2d4a6e 50%,#8ea6c0)"></div>
</article>
<article class="abs service-card" style="left:554px;width:214px">
  <h3>VN Software</h3>
  <p>Tools for sourcing and metrics, coming soon.</p>
  <div class="service-photo" role="img" aria-label="Photo of a man beside a growth and market word board" style="background:linear-gradient(90deg,#1f4f6e,#123349 60%,#2b3340)"></div>
</article>

<section class="abs welcome">
  <h2><span>Welcome to</span> VERDANT NORTH SERVICES</h2>
  <p style="top:27px">ICT sourcing decides how much value large enterprises get from their suppliers. VN Services brings deep knowledge of ICT and business together with the ability to execute, so that the relation between enterprise and supplier becomes a lasting source of value.</p>
  <p style="top:78px">We work for CIOs and boards of directors of enterprises with more than 1000 employees. VN Sourcing selects, contracts and manages ICT suppliers. VN Metrics builds business cases and follows the trends in ICT that shape your next decision. VN Software will add tools that support both sourcing and metrics. Together they help you create and optimize the relations between your organization and its ICT suppliers, from strategy to daily execution.</p>
</section>
<div class="abs portrait-ring"><div class="portrait" role="img" aria-label="Portrait of a smiling consultant in an office"></div></div>

<section class="abs who">
  <div class="abs who-photo" role="img" aria-label="Photo of colleagues shaking hands in a meeting"></div>
  <h2><span class="accent">Who We</span> Are?</h2>
  <p>We are a team of senior ICT and business consultants<br>( Sourcing Strategy, Supplier Selection, Contract Management, Business Case Analysis, ICT Trends, Vendor Governance and Transition Management ) who join expertise in ICT with a strong ability to execute, and who create and optimize the relations between ICT suppliers and large enterprises.</p>
  <a class="more" href="#">more &gt;&gt;</a>
</section>

<section class="abs panel" style="left:87px;width:438px;height:181px">
  <div class="panel-head">ABOUT US</div>
  <h3 style="left:12px;top:36px"><span class="accent">Our</span> Work</h3>
  <p style="left:12px;top:50px;width:310px">we guide enterprises through every step of ICT sourcing<br>( Strategy, Supplier Selection, Contracting, Business Cases, Trend Analysis and Supplier Relation Management )</p>
  <div class="thumb" role="img" aria-label="Illustration of business people climbing a rising line chart" style="left:328px;top:35px;width:95px;height:63px;background:linear-gradient(#f3f3f3,#d7dbe0)"></div>
  <div class="thumb" role="img" aria-label="Photo of two colleagues reviewing a document" style="left:9px;top:108px;width:91px;height:58px;background:linear-gradient(90deg,#cfd3d8,#3a3f48 55%,#a8b0bb)"></div>
  <h3 style="left:113px;top:113px"><span class="accent">Our</span> Clients</h3>
  <p style="left:113px;top:127px;width:310px">large enterprises with more than 1000 employees<br>( CIOs and boards of directors who want ICT suppliers that deliver real business value, every year )</p>
</section>

<section class="abs panel" style="left:535px;width:233px;height:181px">
  <div class="panel-head">INSPIRE</div>
  <div class="topic" style="top:30px"><div class="topic-image" role="img" aria-label="Topic image"></div><div><b>Sourcing insight</b><span>What makes ICT suppliers deliver.</span>
    <div class="stars"><svg width="50" height="9" viewBox="0 0 50 9"><g fill="var(--star)"><path id="st" d="M4.5 0l1.1 3h3.2L6.2 5l1 3.2-2.7-2-2.7 2 1-3.2L.2 3h3.2z"/><use href="#st" x="12.5"/><use href="#st" x="25"/><use href="#st" x="37.5"/></g></svg></div></div></div>
  <div class="topic" style="top:79px"><div class="topic-image" role="img" aria-label="Topic image"></div><div><b>Metrics trend</b><span>Building an ICT case the board trusts.</span>
    <div class="stars"><svg width="38" height="9" viewBox="0 0 38 9"><g fill="var(--star)"><use href="#st"/><use href="#st" x="12.5"/><use href="#st" x="25"/></g></svg></div></div></div>
  <div class="topic" style="top:125px"><div class="topic-image" role="img" aria-label="Topic image"></div><div><b>CIO agenda</b><span>Supplier relations as a strategy.</span>
    <div class="stars"><svg width="50" height="9" viewBox="0 0 50 9"><g fill="var(--star)"><use href="#st"/><use href="#st" x="12.5"/><use href="#st" x="25"/><use href="#st" x="37.5"/></g></svg></div></div></div>
</section>

<div class="abs panel client-head"><div class="panel-head">OUR CLIENT</div></div>
<div class="abs clients">
  <span><i></i>Tamsel</span>
  <span>Orlina store</span>
  <span>Merrow Fashion</span>
  <span>Bravik</span>
  <span>Lumeva</span>
</div>

<footer class="abs footer">
  <div class="foot-col" style="left:107px"><h4>INFORMATION</h4><a href="#">About us</a><a href="#">Privacy Policy</a><a href="#">Term &amp; Conditions</a></div>
  <div class="foot-col" style="left:265px"><h4>OUR SERVICES</h4><a href="#">VN Sourcing</a><a href="#">VN Metrics</a><a href="#">VN Software</a></div>
  <div class="foot-col" style="left:432px"><h4>MY ACCOUNT</h4><a href="#">Sign in</a><a href="#">Register</a><a href="#">Login</a></div>
  <div class="abs newsletter">
    <h4><svg width="14" height="10" viewBox="0 0 14 10"><rect x=".5" y=".5" width="13" height="9" fill="none" stroke="#b6c2d2"/><path d="M.5.5L7 6 13.5.5" fill="none" stroke="#b6c2d2"/></svg>NEWS LETTER SUBSCRIBE</h4>
    <div class="news-form"><div class="field"></div><a class="btn" href="#">Subcribe</a></div>
    <div class="social"><span><i></i>Pixa</span><span><i></i>Friendly</span><span><i></i>Chirpr</span></div>
  </div>
</footer>
<div class="abs bottom-bar">
  <div class="abs copyright">© All Rights Reserved - VN Services - 2013</div>
  <div class="abs payments"><span>Paylo</span><span>Carda</span><span>Linkpay</span></div>
</div>

</body>
</html>
```